New Company Business Card design

Looking for a corporate looking business card utilising my new logo design - the logo i would like embossed as one option and flat as another - simplistic but stylish - less is more - we are an import export business launching into the market - i would like a couple of options as main background - Grey or Black

```html
<!DOCTYPE html>
<html lang="en">
<head>
<meta charset="utf-8">
<title>Meridian Trade Partners – Business Card Options</title>
<link rel="stylesheet" href="https://fonts.googleapis.com/css2?family=Gelasio:wght@400&family=Lato:wght@400;700&display=swap">
<style>
  :root {
    --page: #ffffff;
    --brand-blue: #4a8cc9;
    --ink-muted: #8c8f92;
    --black-base: #0c0c0c;
    --black-light: #2f2f2f;
    --grey-light: #6b6e71;
    --card-w: 401px;
    --card-h: 222px;
  }
  * { box-sizing: border-box; margin: 0; padding: 0; }
  html, body {
    width: 1200px; height: 635px; overflow: hidden;
    background: var(--page);
  }
  .sheet { position: relative; width: 1200px; height: 635px; }

  .card {
    position: absolute;
    width: var(--card-w); height: var(--card-h);
    overflow: hidden;
    box-shadow: 0 4px 10px rgba(0,0,0,0.18);
  }
  .card--black {
    background:
      radial-gradient(ellipse 30% 60% at 30% 45%, rgba(255,255,255,0.05), transparent 70%),
      linear-gradient(90deg, var(--black-light) 0%, #1c1c1c 40%, #111 60%, var(--black-base) 80%, #2c2c2c 100%);
  }
  .card--grey {
    background:
      radial-gradient(ellipse 30% 60% at 30% 45%, rgba(0,0,0,0.05), transparent 70%),
      linear-gradient(90deg, var(--grey-light) 0%, #636669 40%, #5e6164 60%, #4b4e51 80%, #666a6d 100%);
  }
  .front--black { left: 313px; top: 72px; }
  .front--grey  { left: 750px; top: 72px; }
  .back--black  { left: 50px;  top: 327px; }
  .back--grey   { left: 488px; top: 327px; }

  .brand {
    position: absolute; right: 21px; bottom: 30px;
    display: flex; flex-direction: column; align-items: flex-end;
    font-family: "Gelasio", Georgia, serif;
    color: var(--brand-blue);
  }
  .brand__dot {
    width: 40px; height: 40px; border-radius: 50%;
    background: var(--brand-blue);
    margin-bottom: 14px; margin-right: 72px;
  }
  .brand__name {
    font-size: 12.5px; letter-spacing: 0.4px; line-height: 1;
    text-transform: uppercase; white-space: nowrap;
  }

  .person {
    position: absolute; left: 22px; top: 22px;
    font-family: "Gelasio", Georgia, serif;
  }
  .person__name { font-size: 18.5px; color: var(--brand-blue); font-weight: 400; }
  .person__role { font-size: 9.5px; color: var(--ink-muted); margin-top: 3px; }

  .contact { font-family: "Lato", Arial, sans-serif; position: absolute; }
  .contact__web {
    left: 22px; bottom: 24px;
    font-size: 9px; font-weight: 700; color: var(--brand-blue);
  }
  .contact__direct { right: 21px; bottom: 24px; text-align: right; }
  .contact__phone { font-size: 12px; font-weight: 700; color: var(--brand-blue); display: block; }
  .contact__email { font-size: 8.5px; color: var(--ink-muted); display: block; margin-top: 1px; }
</style>
</head>
<body>
<main class="sheet">

  <section class="card card--black front--black" aria-label="Front, black option">
    <div class="brand">
      <span class="brand__dot"></span>
      <span class="brand__name">Meridian Trade Partners</span>
    </div>
  </section>

  <section class="card card--grey front--grey" aria-label="Front, grey option">
    <div class="brand">
      <span class="brand__dot"></span>
      <span class="brand__name">Meridian Trade Partners</span>
    </div>
  </section>

  <section class="card card--black back--black" aria-label="Back, black option">
    <div class="person">
      <h2 class="person__name">Daniel Marlowe</h2>
      <p class="person__role">Marketing Executive</p>
    </div>
    <p class="contact contact__web">meridiantrade.com</p>
    <p class="contact contact__direct">
      <span class="contact__phone">041-5678-290</span>
      <span class="contact__email">d.marlowe@mail.com</span>
    </p>
  </section>

  <section class="card card--grey back--grey" aria-label="Back, grey option">
    <div class="person">
      <h2 class="person__name">Daniel Marlowe</h2>
      <p class="person__role">Marketing Executive</p>
    </div>
    <p class="contact contact__web">meridiantrade.com</p>
    <p class="contact contact__direct">
      <span class="contact__phone">041-5678-290</span>
      <span class="contact__email">d.marlowe@mail.com</span>
    </p>
  </section>

</main>
</body>
</html>
```